Banner Ad for Weight Loss Product Site

We need a banner ad design for a new company selling a weight loss online programme (Ebook). The product is called "Slim Quill" and is suitable for people that want to lose weight fast and without doing sports, regardless of age. We would like to see designs that are eye-catching and at its best animated like in the example files. The final design should exhibit a professional look that encourages the customers to buy our product. The text should be "Persönlicher Diätplan zum Abnehmen?" as a title and "Jetzt informieren" for the button field. Thank you!

```html
<!DOCTYPE html>
<html lang="de">
<head>
<meta charset="utf-8">
<title>Slim Quill – Banner Set</title>
<link href="https://fonts.googleapis.com/css2?family=Arimo:wght@400;700&display=swap" rel="stylesheet">
<style>
  :root {
    --green-top: #79a443;
    --green-mid: #5d8a2f;
    --green-deep: #3c6a1c;
    --green-glow: #8db85a;
    --title-yellow: #f5ee1c;
    --orange-light: #fb8f22;
    --orange-dark: #e2520b;
    --white: #ffffff;
    --label: #222222;
    --photo-a: #c9a184;
    --photo-b: #6b4a36;
    --book-a: #f7f7f2;
    --book-b: #d9dccd;
    --logo-fill: #4f7d27;
  }
  * { box-sizing: border-box; margin: 0; padding: 0; }
  html, body {
    width: 1200px; height: 1200px; overflow: hidden;
    background: var(--white);
    font-family: "Arimo", Arial, sans-serif;
  }
  .sheet { position: relative; width: 1200px; height: 1200px; }

  .banner {
    position: absolute; overflow: hidden;
    background: linear-gradient(180deg, var(--green-top) 0%, var(--green-mid) 55%, var(--green-deep) 100%);
    border: 1px solid #3a5f1d;
  }
  .size-label {
    position: absolute; font-size: 21px; color: var(--label);
    text-align: center; width: 200px;
  }

  .glow {
    position: absolute; border-radius: 50%;
    background: radial-gradient(ellipse at center, var(--green-glow) 0%, rgba(141,184,90,0.75) 60%, rgba(141,184,90,0) 100%);
  }
  .title {
    position: absolute; color: var(--title-yellow);
    font-weight: 700; text-transform: uppercase; line-height: 1.12;
    text-shadow: 1px 2px 2px rgba(0,0,0,0.45);
  }
  .dots {
    position: absolute; height: 0;
    border-top: 3px dotted rgba(255,255,255,0.9);
  }
  .photo {
    position: absolute;
    background: linear-gradient(180deg, var(--photo-b) 0%, var(--photo-a) 45%, #222 78%, var(--photo-a) 100%);
    opacity: 0.9;
  }
  .book {
    position: absolute;
    background: linear-gradient(135deg, var(--book-a) 0%, var(--book-b) 100%);
    box-shadow: 3px 3px 6px rgba(0,0,0,0.35);
  }
  .logo {
    position: absolute; border-radius: 50%;
    background: var(--logo-fill);
    border: 5px solid var(--white);
    display: flex; align-items: center; justify-content: center;
    color: var(--white); font-weight: 700; text-align: center; line-height: 1.05;
  }
  .cta {
    position: absolute; border-radius: 8px;
    background: linear-gradient(180deg, var(--orange-light) 0%, var(--orange-dark) 100%);
    box-shadow: 0 3px 5px rgba(0,0,0,0.35);
    color: var(--white); font-weight: 700;
    display: flex; align-items: center; justify-content: space-between;
    padding: 0 6px 0 10px;
    text-shadow: 0 1px 1px rgba(0,0,0,0.3);
  }
  .cta svg { flex: none; }

  /* leaderboard */
  .leaderboard { left: 71px; top: 52px; width: 1028px; height: 127px; }
  .leaderboard .title { left: 40px; top: 8px; font-size: 28px; }
  /* medium rectangle */
  .rectangle { left: 68px; top: 297px; width: 424px; height: 353px; }
  .rectangle .title { left: 10px; top: 20px; font-size: 31px; }
  /* skyscraper */
  .skyscraper { left: 900px; top: 297px; width: 226px; height: 847px; }
  .skyscraper .title { left: 10px; top: 20px; font-size: 30px; line-height: 1.4; }
  .skyscraper .title .small { font-size: 22px; }
</style>
</head>
<body>
<main class="sheet">

  <!-- 728x90 -->
  <section class="banner leaderboard">
    <div class="glow" style="left:380px; top:-40px; width:520px; height:210px;"></div>
    <h2 class="title">Persönlicher<br>Diätplan zum<br>Abnehmen</h2>
    <div class="photo" role="img" aria-label="Photo of a slim woman measuring her waist" style="left:380px; top:0; width:170px; height:127px;"></div>
    <div class="book" role="img" aria-label="Ebook cover of the diet plan" style="left:555px; top:14px; width:140px; height:113px;"></div>
    <div class="logo" style="left:690px; top:10px; width:104px; height:104px; font-size:19px;">Slim<br>Quill</div>
    <div class="cta" style="left:795px; top:40px; width:215px; height:48px; font-size:17px;">
      <span>Jetzt Informieren</span>
      <svg width="30" height="30" viewBox="0 0 30 30"><circle cx="15" cy="15" r="14" fill="#fff"/><path d="M8 12.5h8v-5l7 7.5-7 7.5v-5H8z" fill="#e8610e"/></svg>
    </div>
  </section>
  <div class="size-label" style="left:485px; top:190px;">728x90</div>

  <!-- 300x250 -->
  <section class="banner rectangle">
    <div class="glow" style="left:230px; top:60px; width:240px; height:300px;"></div>
    <h2 class="title">Persönlicher<br>Diätplan zum<br>Abnehmen</h2>
    <div class="dots" style="left:14px; top:160px; width:180px;"></div>
    <div class="photo" role="img" aria-label="Photo of a smiling woman pointing forward" style="left:292px; top:40px; width:128px; height:313px;"></div>
    <div class="book" role="img" aria-label="Ebook cover of the diet plan" style="left:13px; top:183px; width:152px; height:170px;"></div>
    <div class="logo" style="left:159px; top:150px; width:126px; height:126px; font-size:22px;">Slim<br>Quill</div>
    <div class="cta" style="left:134px; top:287px; width:216px; height:48px; font-size:17px;">
      <span>Jetzt Informieren</span>
      <svg width="30" height="30" viewBox="0 0 30 30"><circle cx="15" cy="15" r="14" fill="#fff"/><path d="M8 12.5h8v-5l7 7.5-7 7.5v-5H8z" fill="#e8610e"/></svg>
    </div>
  </section>
  <div class="size-label" style="left:180px; top:662px;">300X250</div>

  <!-- 160x600 -->
  <section class="banner skyscraper">
    <div class="glow" style="left:0; top:260px; width:226px; height:400px;"></div>
    <h2 class="title"><span class="small">Persönlicher</span><br>Diätplan<br>zum<br>Abnehmen</h2>
    <div class="dots" style="left:14px; top:191px; width:198px;"></div>
    <div class="photo" role="img" aria-label="Photo of a smiling woman pointing forward" style="left:20px; top:205px; width:200px; height:402px;"></div>
    <div class="logo" style="left:52px; top:489px; width:124px; height:124px; font-size:22px;">Slim<br>Quill</div>
    <div class="book" role="img" aria-label="Ebook cover of the diet plan" style="left:35px; top:610px; width:156px; height:177px;"></div>
    <div class="cta" style="left:6px; top:787px; width:214px; height:46px; font-size:17px;">
      <span>Jetzt Informieren</span>
      <svg width="30" height="30" viewBox="0 0 30 30"><circle cx="15" cy="15" r="14" fill="#fff"/><path d="M8 12.5h8v-5l7 7.5-7 7.5v-5H8z" fill="#e8610e"/></svg>
    </div>
  </section>
  <div class="size-label" style="left:913px; top:1154px;">160X600</div>

</main>
</body>
</html>
```